Webdesign für Hausmeisterservice, Garten- und Landschaftsbau
Zielgruppe
Hausmeisterservice und Garten und Landschaftsbau
Aufgabenstellung
habe schon eine Webseite erstellt die muss Designt werden. Wohnpfleger.info

```html
<!DOCTYPE html>
<html lang="de">
<head>
<meta charset="utf-8">
<title>Wohnpfleger – Hausmeister Service</title>
<link href="https://fonts.googleapis.com/css2?family=Open+Sans:wght@400;700&family=Lato:wght@400&display=swap" rel="stylesheet">
<style>
  :root {
    --hero-grey: #ebebeb;
    --hero-light: #f3f3f3;
    --brand-red: #a63c3c;
    --brand-cyan: #1a86b8;
    --brand-blue: #1565a8;
    --footer-blue: #0d62a6;
    --ink: #222222;
    --white: #ffffff;
    --photo-workwear: linear-gradient(135deg, #3a4fb8 0%, #6e7a8c 40%, #2b3fa6 60%, #a8283a 85%, #c43a3f 100%);
    --photo-plumbing: linear-gradient(135deg, #d9dde2 0%, #eef0f2 35%, #c9a48a 70%, #3b56a0 100%);
  }
  * { margin: 0; padding: 0; box-sizing: border-box; }
  html, body { width: 1200px; height: 2259px; overflow: hidden; background: var(--white); }
  body { position: relative; font-family: "Lato", sans-serif; color: var(--ink); }

  .hero { position: absolute; left: 0; top: 0; width: 1200px; height: 675px; background: var(--hero-grey); overflow: hidden; }
  .hero-shapes { position: absolute; inset: 0; }
  .hero-kicker { position: absolute; left: 301px; top: 52px; font-family: "Open Sans", sans-serif; font-weight: 700; font-size: 29px; line-height: 41px; color: var(--brand-red); }
  .brand-name { position: absolute; left: 70px; top: 272px; display: flex; align-items: center; gap: 10px; font-family: "Open Sans", sans-serif; font-weight: 700; font-size: 36px; color: var(--brand-blue); }
  .brand-mark { width: 22px; height: 22px; background: var(--brand-red); }
  .hero-title { position: absolute; left: 69px; top: 383px; font-family: "Open Sans", sans-serif; font-weight: 700; font-size: 42px; line-height: 48px; color: var(--brand-cyan); }

  .intro { position: absolute; left: 341px; top: 733px; width: 520px; }
  .intro p { font-size: 12.3px; line-height: 20.6px; margin-bottom: 20.6px; }
  .intro-cta { font-family: "Open Sans", sans-serif; font-weight: 700; font-size: 24px; line-height: 33px; color: var(--brand-blue); margin-top: -6px; }

  .services-photo { position: absolute; left: 0; top: 1092px; }
  .services-list { position: absolute; left: 349px; top: 1094px; font-family: "Open Sans", sans-serif; font-weight: 700; font-size: 37px; line-height: 62px; color: var(--ink); }
  .services-list .highlight { color: var(--brand-blue); }
  .services-text { position: absolute; left: 750px; top: 1225px; width: 345px; }
  .services-text p { font-size: 12.3px; line-height: 20.6px; margin-bottom: 20.6px; }

  .footer { position: absolute; left: 0; top: 1855px; width: 1200px; height: 404px; background: var(--footer-blue); color: var(--white); font-family: "Open Sans", sans-serif; }
  .footer-heading { position: absolute; left: 95px; top: 40px; font-weight: 700; font-size: 24px; }
  .footer-contact { position: absolute; left: 95px; top: 90px; font-size: 32px; line-height: 48px; }
  .footer-legal { position: absolute; left: 95px; top: 214px; font-size: 20px; line-height: 32.5px; }
  .footer-address { position: absolute; left: 605px; top: 94px; font-size: 20px; line-height: 32.5px; }
  .footer-services { position: absolute; left: 605px; top: 214px; font-size: 20px; line-height: 32.5px; }
</style>
</head>
<body>

<header class="hero">
  <svg class="hero-shapes" width="1200" height="675" viewBox="0 0 1200 675">
    <defs>
      <linearGradient id="workwear" x1="0" y1="0" x2="1" y2="1">
        <stop offset="0" stop-color="#3a4fb8"/>
        <stop offset="0.4" stop-color="#6e7a8c"/>
        <stop offset="0.6" stop-color="#2b3fa6"/>
        <stop offset="0.85" stop-color="#a8283a"/>
        <stop offset="1" stop-color="#c43a3f"/>
      </linearGradient>
    </defs>
    <polygon points="175,0 719,0 439,346" fill="#f3f3f3"/>
    <polygon role="img" aria-label="Foto: Gabelschlüssel und Schraubendreher in der Tasche einer blauen Arbeitshose vor kariertem Hemd" points="719,0 1200,0 1200,675 684,675 439,346" fill="url(#workwear)"/>
  </svg>
  <div class="hero-kicker">GARTEN &amp;<br>LANDSCHAFTSBAU</div>
  <div class="brand-name"><span class="brand-mark"></span>Wohnpfleger</div>
  <h1 class="hero-title">HAUSMEISTER<br>SERVICE</h1>
</header>

<section class="intro">
  <p>Als Hausmeisterservice fühlen wir uns für das gesamte übertragene Objekt verantwortlich. Innen erledigen wir kleine Reparaturen, überwachen die Heizungsanlage und führen bei Bedarf auch Entrümpelungen von Kellern und Wohnungen durch.</p>
  <p>Nach der Entrümpelung renovieren wir die Räume schnell und fachgerecht, sodass sie wieder genutzt werden können. Außen kümmern wir uns um die Zuwegungen, erledigen die Gartenarbeiten ganzjährig und unser Winterdienst sorgt bei Schnee und Glätte für freie und gesicherte Wege.</p>
  <h2 class="intro-cta">WIR FREUEN UNS AUF IHRE ANFRAGE UND IHREN AUFTRAG.</h2>
</section>

<section>
  <svg class="services-photo" width="724" height="596" viewBox="0 0 724 596">
    <defs>
      <linearGradient id="plumbing" x1="0" y1="0" x2="1" y2="1">
        <stop offset="0" stop-color="#d9dde2"/>
        <stop offset="0.35" stop-color="#eef0f2"/>
        <stop offset="0.7" stop-color="#c9a48a"/>
        <stop offset="1" stop-color="#3b56a0"/>
      </linearGradient>
    </defs>
    <polygon role="img" aria-label="Foto: Hand setzt eine Rohrzange an einem verchromten Siphon vor weißen Fliesen an" points="0,0 198,0 724,596 0,596" fill="url(#plumbing)"/>
  </svg>
  <div class="services-list">
    <div>HOUSEKEEPING</div>
    <div>PARTNERSCHAFT</div>
    <div class="highlight">24H SERVICE</div>
  </div>
  <div class="services-text">
    <p>Wer eine Verstopfung im Abfluss bemerkt, der braucht schnelle Hilfe, daher ist unser Service 24 Stunden für sie im Einsatz.</p>
    <p>Sie werden erst über alle anfallenden Kosten informiert und dann wird mit den Arbeiten erst begonnen - keine versteckten Kosten - kostenlose Beratung.</p>
  </div>
</section>

<footer class="footer">
  <h2 class="footer-heading">WIR FREUEN UNS VON IHNEN ZU HÖREN</h2>
  <div class="footer-contact">
    <div>0176 - 520 318 47</div>
    <div>kontakt@wohnpfleger.info</div>
  </div>
  <div class="footer-legal">
    <div>©2023 Jonas Brenner</div>
    <div>Impressum</div>
    <div>Datenschutzerklärung</div>
  </div>
  <address class="footer-address" style="font-style: normal;">
    <div>Jonas Brenner</div>
    <div>Lindenallee 14</div>
    <div>Musterstadt 12345</div>
  </address>
  <div class="footer-services">
    <div>Garten &amp; Landschaftsbau</div>
    <div>Hausmeister Service</div>
  </div>
</footer>

</body>
</html>
```